Electrical panel service sticker w Bucket truck & Logo

We have a rather plain sticker we put on lighting panels to remind customers who to call for service. We want to redesign them with brushed aluminum background. We want a remake of the sticker with the outline of a bucket truck. You'll need to find or draw the outling of a bucket truck maybe with the boom up slightly as we will get these stickers die cut.

We want LOGO with Ph.# and Email.
Electrical * Lighting * Sign Service

Target Market(s)

Commercial property managers

Industry/Entity Type

Property Management

Requirements
Must have
• Bucket Truck Outline

```html
<!DOCTYPE html>
<html lang="en">
<head>
<meta charset="utf-8">
<title>Brightway Service – Panel Service Sticker</title>
<link href="https://fonts.googleapis.com/css2?family=Russo+One&family=Oswald:wght@600&family=Montserrat:wght@800&display=swap" rel="stylesheet">
<style>
  :root {
    --backdrop: #4a4a4a;
    --ink: #262626;
    --rule: #5e5e5e;
    --alu-light: #e9e9e9;
    --alu-mid: #cfcfcf;
    --alu-dark: #9d9d9d;
    --plate-edge: #8a8a8a;
  }
  html, body {
    margin: 0;
    width: 1200px;
    height: 1200px;
    overflow: hidden;
    background: var(--backdrop);
  }
  .sticker {
    position: absolute;
    inset: 0;
    width: 1200px;
    height: 1200px;
  }
  .brand-name { font-family: "Russo One", sans-serif; fill: var(--ink); }
  .brand-sub { font-family: "Russo One", sans-serif; fill: var(--ink); }
  .plaque-label { font-family: "Oswald", sans-serif; font-weight: 600; fill: var(--ink); }
  .plaque-phone { font-family: "Montserrat", sans-serif; font-weight: 800; fill: var(--ink); }
  .web-address { font-family: "Montserrat", sans-serif; font-weight: 800; fill: var(--ink); }
  .service-list { font-family: "Oswald", sans-serif; font-weight: 600; fill: var(--ink); }
</style>
</head>
<body>
<svg class="sticker" viewBox="0 0 1200 1200" xmlns="http://www.w3.org/2000/svg">
  <defs>
    <linearGradient id="edgeMetal" x1="0" y1="0" x2="1" y2="1">
      <stop offset="0" stop-color="#f4f4f4"/>
      <stop offset="0.45" stop-color="#a9a9a9"/>
      <stop offset="0.7" stop-color="#e4e4e4"/>
      <stop offset="1" stop-color="#8f8f8f"/>
    </linearGradient>
    <linearGradient id="brushedFace" x1="0" y1="0" x2="0" y2="1">
      <stop offset="0" stop-color="#d6d6d6"/>
      <stop offset="0.5" stop-color="#e2e2e2"/>
      <stop offset="1" stop-color="#d2d2d2"/>
    </linearGradient>
    <pattern id="brushLines" width="1200" height="4" patternUnits="userSpaceOnUse">
      <rect width="1200" height="1" y="1" fill="#ffffff" opacity="0.25"/>
      <rect width="1200" height="1" y="3" fill="#9a9a9a" opacity="0.12"/>
    </pattern>
    <linearGradient id="plaqueMetal" x1="0" y1="0" x2="0" y2="1">
      <stop offset="0" stop-color="#f2f2f2"/>
      <stop offset="0.5" stop-color="#bdbdbd"/>
      <stop offset="1" stop-color="#e6e6e6"/>
    </linearGradient>
  </defs>

  <!-- die-cut plate -->
  <path class="plate-edge" fill="url(#edgeMetal)" d="M205,266 H994 A146,150 0 0 0 1140,416 V785 A146,150 0 0 0 994,935 H205 A146,150 0 0 0 61,785 V416 A146,150 0 0 0 205,266Z"/>
  <path class="plate-face" fill="url(#brushedFace)" d="M223,284 H976 A164,168 0 0 0 1122,434 V767 A164,168 0 0 0 976,917 H223 A164,168 0 0 0 79,767 V434 A164,168 0 0 0 223,284Z"/>
  <path class="plate-brush" fill="url(#brushLines)" d="M223,284 H976 A164,168 0 0 0 1122,434 V767 A164,168 0 0 0 976,917 H223 A164,168 0 0 0 79,767 V434 A164,168 0 0 0 223,284Z"/>
  <path class="plate-rule" fill="none" stroke="var(--rule)" stroke-width="3" d="M249,310 H950 A190,194 0 0 0 1096,460 V741 A190,194 0 0 0 950,891 H249 A190,194 0 0 0 105,741 V460 A190,194 0 0 0 249,310Z"/>

  <!-- truck illustration area -->
  <rect class="truck-illustration" role="img" aria-label="Line drawing of a flatbed bucket truck with its boom raised" x="487" y="330" width="226" height="95" rx="6" fill="#c4c4c4"/>

  <!-- brand name -->
  <text class="brand-name" x="600" y="497" font-size="90" text-anchor="middle" textLength="600" lengthAdjust="spacingAndGlyphs">BRIGHTWAY</text>
  <text class="brand-name" x="600" y="584" font-size="66" text-anchor="middle" textLength="690" lengthAdjust="spacingAndGlyphs">SERVICE</text>
  <text class="brand-sub" x="600" y="617" font-size="30" text-anchor="middle" textLength="324" lengthAdjust="spacingAndGlyphs">INCORPORATED</text>

  <!-- call plaques -->
  <g class="plaque plaque-label-box">
    <rect x="184" y="643" width="319" height="70" rx="5" fill="url(#plaqueMetal)" stroke="#8a8a8a" stroke-width="2"/>
    <circle cx="194" cy="653" r="2.5" fill="#7a7a7a"/><circle cx="493" cy="653" r="2.5" fill="#7a7a7a"/>
    <circle cx="194" cy="703" r="2.5" fill="#7a7a7a"/><circle cx="493" cy="703" r="2.5" fill="#7a7a7a"/>
    <text class="plaque-label" x="344" y="694" font-size="40" text-anchor="middle" textLength="268" lengthAdjust="spacingAndGlyphs">FOR SERVICES CALL</text>
  </g>
  <g class="plaque plaque-phone-box">
    <rect x="511" y="643" width="506" height="70" rx="5" fill="url(#plaqueMetal)" stroke="#8a8a8a" stroke-width="2"/>
    <circle cx="521" cy="653" r="2.5" fill="#7a7a7a"/><circle cx="1007" cy="653" r="2.5" fill="#7a7a7a"/>
    <circle cx="521" cy="703" r="2.5" fill="#7a7a7a"/><circle cx="1007" cy="703" r="2.5" fill="#7a7a7a"/>
    <text class="plaque-phone" x="764" y="697" font-size="52" text-anchor="middle" textLength="450" lengthAdjust="spacingAndGlyphs">800–555–0142</text>
  </g>

  <!-- web address -->
  <text class="web-address" x="600" y="772" font-size="40" text-anchor="middle" textLength="724" lengthAdjust="spacingAndGlyphs">www.brightwayservice.com</text>

  <!-- services -->
  <g class="service-list">
    <circle cx="291" cy="825" r="6" fill="#ededed" stroke="#9a9a9a"/>
    <text x="306" y="843" font-size="44" textLength="160" lengthAdjust="spacingAndGlyphs">Electrical</text>
    <circle cx="502" cy="825" r="6" fill="#ededed" stroke="#9a9a9a"/>
    <text x="517" y="843" font-size="44" textLength="135" lengthAdjust="spacingAndGlyphs">Lighting</text>
    <circle cx="690" cy="825" r="6" fill="#ededed" stroke="#9a9a9a"/>
    <text x="706" y="843" font-size="44" textLength="210" lengthAdjust="spacingAndGlyphs">Sign Service</text>
  </g>
</svg>
</body>
</html>
```